Business Card & Logo Design - Marketing services for building industry

A freelance marketing & communications specialist focused on bid writing & publications, events & sponsorship, PR & marketing strategy and digital media projects.

Working with small business owners or individuals that need some additional help for short assignments and contracts. Industry specialties include building, construction & property and professional services.

“I can help you with one-off or ongoing marketing projects to suit your budget.”

Target Market(s)

Magazine editors, Trade suppliers, Consultants, Builders, Business Owners and Private Home Owners

Industry/Entity Type

Communications

Contact Information for Business Card

Keen Frame PR
Copywriting & Marketing Services
keenframepr-example.com.au
PO Box 913
Harlow Park QLD 4975
Delia Harwick
delia@keenframepr-example.com.au
0455 193 672

Colors

Designer to choose colors to be used in the design.

Requirements
Must have
• Important to have logo/image similar to the attachments but with wire light bulb shaped to include some residential houses (with a dormer window outline on roof). Business name to be underneath. Simple colour choices in logo, say 2, plus a background. Include a geometric drawing of light bulb at far right end if possible but keep small enough for transfer to an e-signature.
Nice to have
• Architectural look with clean lines.
Should not have
• Please don't include anything feminine, as the building industry is male dominated.

```html
<!DOCTYPE html>
<html lang="en">
<head>
<meta charset="utf-8">
<title>Keen Frame PR – Business Card</title>
<link rel="stylesheet" href="https://fonts.googleapis.com/css2?family=Roboto+Slab:wght@400;500&family=Open+Sans:wght@400&family=Courier+Prime:wght@400&display=swap">
<style>
  :root {
    --stage: #d9d9d9;
    --card-dark: #0b0b0b;
    --card-light: #f4f4f2;
    --ink-light: #ffffff;
    --ink-dark: #1f1f1f;
    --accent: #c4242b;
    --rule: #8a8a8a;
  }
  html, body {
    margin: 0;
    padding: 0;
    width: 1200px;
    height: 3000px;
    overflow: hidden;
    background: var(--stage);
  }
  .canvas {
    position: relative;
    width: 1200px;
    height: 3000px;
  }
  .card {
    position: absolute;
    left: 80px;
    width: 1040px;
    height: 636px;
    box-sizing: border-box;
    box-shadow: 0 18px 40px rgba(0,0,0,0.25);
  }
  .card--front {
    top: 560px;
    background: var(--card-dark);
    display: flex;
    align-items: center;
    justify-content: center;
  }
  .card--back {
    top: 1800px;
    background: var(--card-light);
    display: flex;
    align-items: center;
    padding: 0 56px;
  }

  /* Brand lockup */
  .brand {
    display: flex;
    flex-direction: column;
    align-items: flex-start;
  }
  .brand__row {
    display: flex;
    align-items: center;
    gap: 22px;
  }
  .brand__square {
    background: var(--accent);
    flex: none;
  }
  .brand__name {
    font-family: "Roboto Slab", Georgia, serif;
    font-weight: 500;
    line-height: 1;
    white-space: nowrap;
  }
  .brand__tagline {
    font-family: "Open Sans", Arial, sans-serif;
    font-weight: 400;
    letter-spacing: 0.08em;
    white-space: nowrap;
  }

  .card--front .brand__square { width: 54px; height: 54px; }
  .card--front .brand__name { font-size: 104px; color: var(--ink-light); }
  .card--front .brand__tagline {
    font-size: 36px;
    color: var(--ink-light);
    margin-top: 18px;
    margin-left: 76px;
  }

  .card--back .brand { width: 372px; flex: none; }
  .card--back .brand__square { width: 24px; height: 24px; }
  .card--back .brand__row { gap: 12px; }
  .card--back .brand__name { font-size: 42px; color: var(--ink-dark); }
  .card--back .brand__tagline {
    font-size: 15px;
    color: var(--ink-dark);
    margin-top: 8px;
    margin-left: 36px;
  }

  .divider {
    width: 2px;
    height: 300px;
    background: var(--rule);
    margin: 0 36px 0 20px;
    flex: none;
  }

  /* Contact block */
  .contact {
    font-family: "Courier Prime", "Courier New", monospace;
    color: var(--ink-dark);
    font-size: 20px;
    line-height: 1.35;
    white-space: nowrap;
  }
  .contact__name {
    font-family: "Roboto Slab", Georgia, serif;
    font-weight: 500;
    font-size: 32px;
    color: var(--accent);
    text-transform: uppercase;
    margin: 0;
    letter-spacing: 0.01em;
  }
  .contact__role {
    margin: 2px 0 20px;
  }
  .contact__list {
    list-style: none;
    margin: 0 0 30px;
    padding: 0;
  }
  .contact__label {
    color: var(--accent);
    margin-right: 8px;
  }
  .contact__address {
    font-style: normal;
  }
</style>
</head>
<body>
<main class="canvas">

  <section class="card card--front" aria-label="Card front">
    <div class="brand">
      <div class="brand__row">
        <span class="brand__square" aria-hidden="true"></span>
        <span class="brand__name">Keen Frame PR</span>
      </div>
      <span class="brand__tagline">copywriting &amp; marketing services</span>
    </div>
  </section>

  <section class="card card--back" aria-label="Card back">
    <div class="brand">
      <div class="brand__row">
        <span class="brand__square" aria-hidden="true"></span>
        <span class="brand__name">Keen Frame PR</span>
      </div>
      <span class="brand__tagline">copywriting &amp; marketing services</span>
    </div>

    <div class="divider" aria-hidden="true"></div>

    <div class="contact">
      <h2 class="contact__name">Delia Harwick</h2>
      <p class="contact__role">Freelance writer &amp; consultant</p>
      <ul class="contact__list">
        <li><span class="contact__label">M:</span>0455 193 672</li>
        <li><span class="contact__label">E:</span>delia@keenframepr-example.com.au</li>
        <li><span class="contact__label">W:</span>keenframepr-example.com.au</li>
      </ul>
      <address class="contact__address">PO Box 913 Harlow Park<br>QLD 4975</address>
    </div>
  </section>

</main>
</body>
</html>
```